Wordpress Theme Design for Family Law Firm

Hello, this is a WordPress theme design project, for a "Calmwater Family Mediation" practice.

I'd want the wordpress theme to be modeled loosely on this existing design from another one of our own sites: http://www.harbor-ledger-replies.example/

We want it to be bright and vibrant and convey a happy and relaxed feeling. The lines on it to not be sharp so more of the rounded edges and subtle shadows that you see on the example site.

Although built on WordPress, the site will be mostly static with fixed content pages, but including a blog feature.

The images will need to be different, but conveying a similar look and feel as the sample site. The colors from the sample site are close to what I'd like - but open to creative options.

It's important that the site looks professional, as well as friendly, and conveys the idea of mediation and relationships.

Important note: Traditional divorce website is for people looking to fight or being bullied.

Divorce mediation is for couples who have decided to split amicably so they're in a much more cooperative state of mind. There's not as much stress and anger. It's just about HOW we go about finalizing the process. There's light at the end of the tunnel.

With that in mind, the site should look friendly and happy, with an inspiring theme of a bright future.

Target Market(s)

The target market are people looking for amicable resolution, with a happy and uplifting attitude..

Traditional divorce websites are for people generally looking to fight or being bullied.

Divorce mediation (this website) is for couples who have decided to split amicably so they're in a much more cooperative state of mind. There's not as much stress and anger. It's just about HOW we go about finalizing the process. There's light at the end of the tunnel.

Industry/Entity Type

Family Law

Requirements
Must have
• Must have option for 1 or two sidebars for pages. This is because some of the internal pages will only have a single sidebar.

The footer will have the option for widgets.

```html
<!DOCTYPE html>
<html lang="en">
<head>
<meta charset="utf-8">
<title>Calmwater Family Mediation</title>
<link href="https://fonts.googleapis.com/css2?family=Play:wght@400;700&display=swap" rel="stylesheet">
<style>
:root{
  --navy:#0b3f7c;
  --navy-dark:#073064;
  --brand:#0c4fa0;
  --btn:#1c3f8f;
  --ink:#4a4a4a;
  --body:#555;
  --band:#f3f2ee;
  --frame:#d6d6d6;
  --grey-box:#c9cdd4;
  --link:#d6451c;
  --black:#050505;
}
*{box-sizing:border-box;margin:0;padding:0}
html,body{width:862px;height:1200px;overflow:hidden;background:#fff}
body{position:relative;font-family:Arial,Helvetica,sans-serif;color:var(--body)}
.abs{position:absolute}
.head-font{font-family:'Play',Arial,sans-serif}
.logo{left:87px;top:26px;font-family:'Play',Arial,sans-serif;font-weight:700;font-size:18px;color:var(--brand);letter-spacing:.2px}
.search{left:594px;top:20px;width:179px;height:23px;border:1px solid #cfcfcf;border-radius:3px;background:#fff}
.search span{position:absolute;left:7px;top:6px;font-size:8px;color:#999}
.search .btn{position:absolute;right:0;top:0;width:24px;height:21px;border-left:1px solid #cfcfcf;background:#f0f0f0;border-radius:0 3px 3px 0}
.nav{left:86px;top:71px;width:690px;height:39px;background:linear-gradient(#164f92,var(--navy-dark));border-radius:3px 3px 0 0;display:flex}
.nav a{color:#fff;text-decoration:none;font-family:'Play',Arial,sans-serif;font-size:9.5px;display:flex;align-items:center;justify-content:center;border-right:1px solid #2d5f9c}
.nav a:last-child{border-right:none}
.band{left:0;top:110px;width:862px;height:407px;background:var(--band)}
.slider{left:86px;top:114px;width:691px;height:270px;background:#fff;border:1px solid var(--frame)}
.slide{position:absolute;left:3px;top:3px;width:683px;height:260px;background:linear-gradient(110deg,#2f3a44 0%,#6d7f8c 35%,#c9d2db 55%,#3b4a5c 75%,#1f2833 100%)}
.dots{left:396px;top:354px;width:71px;height:25px;background:#fff;border-radius:5px 5px 0 0;display:flex;gap:6px;align-items:center;justify-content:center}
.dots i{width:8px;height:8px;border-radius:50%;background:#222}
.dots i:first-child{background:#1c3f8f}
.feature{top:391px;width:161px;height:86px;background:#fff;border:1px solid var(--frame)}
.feature div{position:absolute;left:4px;top:4px;width:151px;height:76px}
.feature-title{top:482px;font-family:'Play',Arial,sans-serif;font-weight:700;font-size:13.5px;color:var(--brand)}
.newsletter{left:587px;top:391px;width:190px;height:86px;background:var(--grey-box)}
.newsletter h3{position:absolute;left:8px;top:8px;font-family:'Play',Arial,sans-serif;font-weight:400;font-size:11.5px;color:var(--brand)}
.newsletter .field{position:absolute;left:5px;top:25px;width:180px;height:23px;background:#fff;border-radius:3px;font-size:8.5px;color:#333;padding:7px 7px}
.newsletter .sub{position:absolute;left:51px;top:57px;width:85px;height:20px;background:var(--btn);border-radius:3px;color:#fff;font-size:8.5px;text-align:center;line-height:20px;border:1px solid #0d2b6b}
h1.welcome{left:87px;top:527px;font-family:'Play',Arial,sans-serif;font-weight:700;font-size:19px;color:#4b4b4b}
.intro{left:87px;top:556px;width:494px;font-size:8px;line-height:13px;color:var(--body)}
.button{top:634px;width:85px;height:20px;background:var(--btn);border:1px solid #0d2b6b;border-radius:2px;color:#fff;font-size:8.5px;text-align:center;line-height:19px}
h2.section{left:87px;top:674px;font-family:'Play',Arial,sans-serif;font-weight:700;font-size:19px;color:#4b4b4b}
.service-thumb{width:83px;height:73px;background:#fff;border:1px solid var(--frame)}
.service-thumb div{position:absolute;left:4px;top:4px;width:73px;height:63px}
.service h3{font-family:Arial,sans-serif;font-weight:700;font-size:12.5px;color:#4b4b4b;margin-bottom:2px}
.service p{font-size:8px;line-height:13px;width:155px}
.side-h{font-family:'Play',Arial,sans-serif;font-weight:700;font-size:13.5px;color:var(--brand)}
.side-p{font-size:8px;line-height:13px;color:var(--body)}
.rule{height:1px;background:#ccc;width:190px;left:587px}
.read{font-size:7px;color:var(--link);text-decoration:underline;display:flex;align-items:center;gap:4px;margin-top:4px}
.read b{width:7px;height:7px;border:1px solid #999;font-size:6px;line-height:5px;text-align:center;color:#555;text-decoration:none;font-weight:400}
.social{top:862px;width:17px;height:17px;border-radius:2px}
.footer{left:0;top:917px;width:862px;height:237px;background:var(--navy)}
.fcol{top:944px;width:143px;color:#fff}
.fcol h4{font-family:Arial,sans-serif;font-weight:700;font-size:14px;padding-bottom:4px;border-bottom:1px solid #7d9cc4;margin-bottom:6px}
.fcol p{font-size:7.5px;line-height:13px;margin-bottom:13px}
.fthumb{position:absolute;width:43px;height:38px}
.copyright{left:0;top:1154px;width:862px;height:46px;background:var(--black);color:#fff;font-size:9.5px;text-align:center;line-height:46px}
</style>
</head>
<body>

<div class="abs logo">CALMWATER FAMILY MEDIATION</div>
<div class="abs search"><span>Search</span><div class="btn">
<svg width="24" height="21" viewBox="0 0 24 21"><circle cx="11" cy="9.5" r="4" fill="none" stroke="#888" stroke-width="1.5"/><line x1="14" y1="12.5" x2="17" y2="15.5" stroke="#888" stroke-width="2"/></svg></div></div>

<nav class="abs nav">
  <a style="width:64px">HOME</a>
  <a style="width:101px">FIRM OVERVIEW</a>
  <a style="width:123px">ATTORNEY PROFILE</a>
  <a style="width:90px">BANKRUPTCY</a>
  <a style="width:97px">TESTIMONIALS</a>
  <a style="width:64px">BLOG</a>
  <a style="width:80px">CONTACT US</a>
</nav>

<div class="abs band"></div>
<div class="abs slider"><div class="slide" role="img" aria-label="Photo of two professionals reviewing and signing documents at a desk"></div></div>
<div class="abs dots"><i></i><i></i><i></i></div>

<div class="abs feature" style="left:86px"><div role="img" aria-label="Photo of a couple shaking hands with an advisor" style="background:linear-gradient(120deg,#e9edf0,#9aa6b1 60%,#5a6470)"></div></div>
<div class="abs feature" style="left:252px"><div role="img" aria-label="Photo of a family advisor meeting with clients" style="background:linear-gradient(120deg,#f1f2f2,#a9a59e 55%,#5e5d5c)"></div></div>
<div class="abs feature" style="left:420px"><div role="img" aria-label="Photo of a couple in an amicable meeting with a mediator" style="background:linear-gradient(120deg,#8e98a3,#c3ccd5 50%,#4a525d)"></div></div>
<div class="abs feature-title" style="left:88px">Professional Approach</div>
<div class="abs feature-title" style="left:254px">Family Advisor</div>
<div class="abs feature-title" style="left:421px">Amicable Divorce</div>

<div class="abs newsletter">
  <h3>Join Our Newsletter</h3>
  <div class="field">Newsletter..</div>
  <div class="sub">Subcribe</div>
</div>

<h1 class="abs welcome">Welcome To Calmwater Family Mediation</h1>
<p class="abs intro">It is a long established fact that a reader will be distracted by the readable content of a page when looking at its layout. The point of using Lorem Ipsum is that it has a more-or-less normal distribution of letters, as opposed to using 'Content here, content here', making it look like readable English. Many desktop publishing packages and web page editors now use Lorem Ipsum as their default model text, and a search for 'lorem ipsum' will uncover many web sites still in their infancy. Various versions have evolved over the years, sometimes by accident, sometimes on purpose (injected humour and the like).</p>
<div class="abs button" style="left:86px">READ MORE</div>
<div class="abs button" style="left:179px">VIRTUAL TOUR</div>

<h2 class="abs section">What We Do</h2>

<div class="abs service-thumb" style="left:86px;top:712px"><div role="img" aria-label="Photo of a father with his children" style="background:linear-gradient(135deg,#c9d6e2,#b88a6e 60%,#6b5446)"></div></div>
<div class="abs service" style="left:171px;top:710px"><h3>Family Law</h3><p>Lorem Ipsum is simply dummy text of the printing and typesetting industry. Lorem Ipsum has been the industry's standard dummy text ever since the</p></div>
<div class="abs service-thumb" style="left:335px;top:712px"><div role="img" aria-label="Photo of clients in a conference meeting" style="background:linear-gradient(135deg,#2b2a28,#6d5c49 55%,#c7b49a)"></div></div>
<div class="abs service" style="left:420px;top:710px"><h3>Our Clients</h3><p>Lorem Ipsum is simply dummy text of the printing and typesetting industry. Lorem Ipsum has been the industry's standard dummy text ever since the</p></div>
<div class="abs service-thumb" style="left:86px;top:806px"><div role="img" aria-label="Photo of a woman working at a desk" style="background:linear-gradient(135deg,#eef3f5,#c9d8de 50%,#8fa6b0)"></div></div>
<div class="abs service" style="left:171px;top:804px"><h3>Personal Solution</h3><p>Lorem Ipsum is simply dummy text of the printing and typesetting industry. Lorem Ipsum has been the industry's standard dummy text ever since the</p></div>
<div class="abs service-thumb" style="left:335px;top:806px"><div role="img" aria-label="Photo of a lawyer in a library office" style="background:linear-gradient(135deg,#5a2a1c,#2a1b16 55%,#8b6a50)"></div></div>
<div class="abs service" style="left:420px;top:804px"><h3>Hiring A Lawyer</h3><p>Lorem Ipsum is simply dummy text of the printing and typesetting industry. Lorem Ipsum has been the industry's standard dummy text ever since the</p></div>

<div class="abs side-h" style="left:587px;top:528px">Testimonials</div>
<svg class="abs" style="left:584px;top:543px" width="16" height="16" viewBox="0 0 16 16"><text x="0" y="16" font-size="22" font-family="Georgia,serif" fill="#d8d8d8">“</text></svg>
<p class="abs side-p" style="left:596px;top:557px;width:168px">Lorem Ipsum is simply dummy text of the printing and typesetting industry. Lorem Ipsum has been the industry's standard dummy text ever since the 1500s,</p>
<svg class="abs" style="left:735px;top:592px" width="16" height="16" viewBox="0 0 16 16"><text x="0" y="20" font-size="22" font-family="Georgia,serif" fill="#d8d8d8">”</text></svg>
<div class="abs rule" style="top:622px"></div>

<div class="abs side-h" style="left:587px;top:634px">Latest Reviews</div>
<div class="abs side-p" style="left:588px;top:655px;width:175px">Lorem Ipsum is simply dummy text of the printing and typesetting industry.<div class="read"><b>+</b>Read More</div></div>
<div class="abs side-p" style="left:588px;top:717px;width:175px">Lorem Ipsum is simply dummy text of the printing and typesetting industry.<div class="read"><b>+</b>Read More</div></div>
<div class="abs side-p" style="left:588px;top:780px;width:175px">Lorem Ipsum is simply dummy text of the printing and typesetting industry.<div class="read"><b>+</b>Read More</div></div>
<div class="abs rule" style="top:829px"></div>
<div class="abs head-font" style="left:587px;top:837px;font-size:9px;color:var(--brand)">Follow Us On The Web:</div>
<div class="abs social" style="left:587px;background:#3b5a98"></div>
<div class="abs social" style="left:608px;background:#3aa3d9"></div>
<div class="abs social" style="left:629px;background:#e8832a"></div>
<div class="abs social" style="left:649px;background:#3a3a3a"></div>

<div class="abs footer"></div>
<div class="abs fcol" style="left:87px">
  <h4>About Us</h4>
  <p>Lorem Ipsum is simply dummy text of the printing and typesetting industry. Lorem Ipsum has been the industry's standard dummy text ever since the 1500s,</p>
  <p>Lorem Ipsum is simply dummy text of the printing and typesetting industry.</p>
  <p>Lorem Ipsum is simply dummy text of the printing and typesetting industry. Lorem Ipsum has been the industry's standard dummy text ever since the 1500s,</p>
</div>
<div class="abs fcol" style="left:267px">
  <h4>From Our Blog</h4>
  <p>Lorem Ipsum is simply dummy text of the printing and typesetting industry. Lorem Ipsum has been the industry's standard dummy text ever since the 1500s,</p>
  <p>Lorem Ipsum is simply dummy text of the printing and typesetting industry.</p>
  <p>Lorem Ipsum is simply dummy text of the printing and typesetting industry. 1500s,</p>
</div>
<div class="abs fcol" style="left:451px">
  <h4>Simple Text Heading</h4>
  <div style="position:relative">
    <div role="img" aria-label="Photo of a gavel" style="float:left;width:38px;height:32px;margin:0 3px 0 2px;background:linear-gradient(135deg,#7a3a14,#d08a44)"></div>
    <p>Lorem Ipsum is simply dummy text of the printing and typesetting industry. Lorem Ipsum has been the industry's standard dummy text ever since the 1500s,</p>
    <div role="img" aria-label="Photo of a smiling couple" style="float:left;width:38px;height:32px;margin:0 3px 0 2px;background:linear-gradient(135deg,#d9d2c8,#8a6a55)"></div>
    <p>Lorem Ipsum is simply dummy text of the printing and typesetting industry. Lorem Ipsum has been the industry's standard dummy text ever since the</p>
  </div>
</div>
<div class="abs fcol" style="left:633px">
  <h4>Simple Text Heading</h4>
</div>
<div class="abs" style="left:633px;top:972px;width:145px;height:145px">
  <div class="fthumb" role="img" aria-label="Photo of an office" style="left:0;top:0;background:linear-gradient(135deg,#3b4450,#9aa3ad)"></div>
  <div class="fthumb" role="img" aria-label="Photo of a divorce document with gavel" style="left:50px;top:0;background:linear-gradient(135deg,#f3f0ec,#b7a89a)"></div>
  <div class="fthumb" role="img" aria-label="Photo of a woman writing" style="left:100px;top:0;background:linear-gradient(135deg,#c98f74,#f2ece8)"></div>
  <div class="fthumb" role="img" aria-label="Photo of divorce papers and pen" style="left:0;top:53px;background:linear-gradient(135deg,#f1eeea,#c2b8ae)"></div>
  <div class="fthumb" role="img" aria-label="Photo of a consultation meeting" style="left:50px;top:53px;background:linear-gradient(135deg,#e6eaee,#4b5561)"></div>
  <div class="fthumb" role="img" aria-label="Photo of a mother and child" style="left:100px;top:53px;background:linear-gradient(135deg,#e8ddd2,#b98c72)"></div>
  <div class="fthumb" role="img" aria-label="Photo of a magnifying glass on text" style="left:0;top:106px;background:linear-gradient(135deg,#d7d7d7,#6a6a6a)"></div>
  <div class="fthumb" role="img" aria-label="Photo of scales of justice" style="left:50px;top:106px;background:linear-gradient(135deg,#3a1c0c,#d2862f)"></div>
  <div class="fthumb" role="img" aria-label="Photo of hands signing a contract" style="left:100px;top:106px;background:linear-gradient(135deg,#1f3550,#8da3bb)"></div>
</div>

<div class="abs copyright">Copyright © 2012 -Calmwater Family Mediation.All Rights Reserved</div>

</body>
</html>
```